Business Card for Financial Asset Management Company

Now we are launching a new company based in Tokyo.
The company information is below;

Company Name: Talvane Management

Operations: Financial assets management, Proposing forming portfolio of assets, Consulting service, and advising to enhance your company's financial health

Corporate Colour: Japan Blue or Navy like below
http://staffpages.qorvenly.edu/mtavis/images/Slate/Teal-Slate-217.jpg

It's dark and deep, and will get to fit to our clients as our relationships last longer and longer.

Our images for this colour are "Japanese style" and "pride in our craftmanship" , and also "gentle".

Corporate Key Image: an order taker who is sincere, polite, but courageous

We don't have our logo yet so please feel free to put any symbol on your design.

Please do not hesitate about asking any questions.
Thank you :-)

Reason: We are still discussin on final decision. Thank you for your understanding.

```html
<!DOCTYPE html>
<html lang="en">
<head>
<meta charset="utf-8">
<title>Talvane Management – Business Card</title>
<link href="https://fonts.googleapis.com/css2?family=PT+Sans:wght@400;700&display=swap" rel="stylesheet">
<style>
  :root {
    --navy-deep: #12122a;
    --indigo: #2e2870;
    --indigo-text: #2d2a72;
    --ink: #16163a;
    --paper: #ffffff;
    --stage-light: #f4f4f4;
    --stage-dark: #cfcfcf;
  }
  html, body {
    margin: 0;
    padding: 0;
    width: 1200px;
    height: 1000px;
    overflow: hidden;
  }
  body {
    position: relative;
    background: radial-gradient(ellipse at 30% 45%, var(--stage-light) 0%, #e3e3e3 45%, var(--stage-dark) 100%);
    font-family: "PT Sans", "Segoe UI", sans-serif;
  }
  .card {
    position: absolute;
    overflow: hidden;
    box-shadow: 0 2px 6px rgba(0,0,0,0.28);
  }

  /* Front */
  .card-front {
    left: 99px;
    top: 84px;
    width: 712px;
    height: 415px;
    background: linear-gradient(90deg, var(--navy-deep) 0%, #22205a 30%, var(--indigo) 52%, #22205a 74%, var(--navy-deep) 100%);
  }
  .front-mark {
    position: absolute;
    left: 343px;
    top: 222px;
    width: 26px;
    height: 26px;
    background: var(--paper);
  }
  .front-name {
    position: absolute;
    left: 0;
    right: 0;
    top: 280px;
    text-align: center;
    color: var(--paper);
    font-weight: 700;
    font-size: 25px;
    letter-spacing: 0.1px;
  }

  /* Back */
  .card-back {
    left: 409px;
    top: 522px;
    width: 729px;
    height: 426px;
    background: var(--paper);
  }
  .back-wave {
    position: absolute;
    left: 0;
    top: 0;
    width: 729px;
    height: 426px;
  }
  .back-brand {
    position: absolute;
    left: 186px;
    top: 120px;
    display: flex;
    align-items: center;
    gap: 14px;
  }
  .back-brand .mark {
    width: 22px;
    height: 22px;
    background: var(--ink);
  }
  .back-brand .name {
    color: var(--indigo-text);
    font-weight: 700;
    font-size: 25px;
  }
  .holder {
    position: absolute;
    left: 132px;
    top: 314px;
    color: var(--paper);
  }
  .holder .person {
    font-weight: 700;
    font-size: 23px;
    line-height: 1.2;
  }
  .holder .role {
    font-size: 17px;
    margin-top: 2px;
  }
  .divider {
    position: absolute;
    left: 323px;
    top: 265px;
    width: 1px;
    height: 141px;
    background: rgba(255,255,255,0.6);
  }
  .contact {
    position: absolute;
    left: 349px;
    top: 260px;
    color: var(--paper);
    font-size: 17px;
    line-height: 26px;
  }
  .contact .address { margin-bottom: 10px; }
  .contact .line {
    display: flex;
    align-items: center;
    gap: 12px;
    margin-left: 6px;
    margin-bottom: 4px;
  }
  .contact svg { width: 17px; height: 14px; fill: var(--paper); }
</style>
</head>
<body>

<section class="card card-front" aria-label="Card front">
  <div class="front-mark"></div>
  <div class="front-name">Talvane Management</div>
</section>

<section class="card card-back" aria-label="Card back">
  <svg class="back-wave" viewBox="0 0 729 426" aria-hidden="true">
    <defs>
      <linearGradient id="bandFill" x1="0" x2="1" y1="0" y2="0">
        <stop offset="0" stop-color="#12122a"/>
        <stop offset="0.45" stop-color="#2e2870"/>
        <stop offset="1" stop-color="#14142e"/>
      </linearGradient>
    </defs>
    <path d="M0 213 C 120 250, 200 262, 330 240 C 470 214, 600 186, 729 212 L 729 426 L 0 426 Z" fill="url(#bandFill)"/>
    <path d="M12 206 C 130 248, 220 256, 340 232 C 470 205, 590 170, 719 204 C 600 176, 470 196, 340 222 C 220 248, 130 246, 12 206 Z" fill="url(#bandFill)"/>
  </svg>

  <div class="back-brand">
    <div class="mark"></div>
    <div class="name">Talvane Management</div>
  </div>

  <div class="holder">
    <div class="person">Haruka Tanabe</div>
    <div class="role">Financial Advisor</div>
  </div>

  <div class="divider"></div>

  <div class="contact">
    <div class="address">Kasumi Hill Building, 2-4-7<br>Nihonbashi Chuo-ku, Tokyo</div>
    <div class="line">
      <svg viewBox="0 0 17 14" aria-label="Phone"><path d="M1 4 C1 1.5 4 0.5 8.5 0.5 C13 0.5 16 1.5 16 4 L13 5 L12 3 C10 2.5 7 2.5 5 3 L4 5 Z"/><path d="M4 6 L13 6 L15 13 L2 13 Z"/></svg>
      <span>81-3-5820-4417</span>
    </div>
    <div class="line">
      <svg viewBox="0 0 17 14" aria-label="Fax"><rect x="4" y="0.5" width="9" height="4"/><rect x="1" y="5" width="15" height="6" rx="1"/><rect x="4" y="9" width="9" height="4.5" fill="#2e2870" stroke="#fff" stroke-width="1"/></svg>
      <span>81-3-5820-44190</span>
    </div>
    <div class="line">
      <svg viewBox="0 0 17 14" aria-label="Email"><rect x="1.5" y="2" width="14" height="10" fill="none" stroke="#fff" stroke-width="1.2"/><path d="M1.5 2 L8.5 8 L15.5 2" fill="none" stroke="#fff" stroke-width="1.2"/></svg>
      <span>info@talvanemanagement.jp</span>
    </div>
  </div>
</section>

</body>
</html>
```